“Be Part Of History! Great Web Design Needed For Local Business!”

Note: This is for design only. No coding required. We want to see your ideas for a great website! This will be a FUN design and not boring like others you may work on.

WE HAVE HAD ONLY 8 DESIGNERS SO FAR SUBMIT - THIS IS A WIDE OPEN CONTEST THAT COULD MAKE YOU GOOD MONEY. PLEASE CONSIDER JOINING!

Look we are needing a great website design for a local carpet cleaning business….I know you are asking how can you “be part of history” with a boring industry like carpet cleaning. Here is the deal….NO ONE in our city has a great design so when you are chosen as the designer you are literally making history by bringing a great design to our city in this industry…

I know it’s cheesy but I am trying to get you to use your skills to help us and make it fun at the same time.

Why work with us:

We are a professional company that has run hundreds of crowdsourced projects on multiple platforms. If you participate in this contest (we hope you do) you can expect great video feedback, consistent feedback, and also our guarantee that if we know your website design will not be what we are looking for we will notify you so you don’t waste your time if there is no chance of you winning.

We respect and recognize this is how you make your living and we will not play games. We look forward to an awesome contest and awesome website designs.

Design Brief:

For this project please let your creative ideas flow. We have given you a ton of info along with videos to help you understand what we are after, however we WANT your creativity to shine through in your designs!

We are looking for a fresh and fun new design for

http://www.brightloomcarpets.example/

This is a local carpet cleaning company that does great work. Unfortunately the current web design is old, outdates, and looks like dirt. So how can they portray a great image with the site they currently have? They can’t so that is why we need your help.

This website needs to convey trust, professionalism, and be super clean and easy to navigate. People making decisions for carpet cleaners are doing this fast so we need to make the site stand out and easy to navigate.

As you can see the current site does not convey trust, looks amateur and does not make people believe that this business has been in business 20 years…this is actually the top company in Albuquerque, but the current site does not reflect that…

Here is a video to help explain what we like about the current site and what we don’t like:

http://clipvista.example/t/qWm4Lp8R

Here are some examples of other sites in their business that have some things we like:

http://www.freshwavecarpet.example/ Please watch video to learn what we like and don’t like:
http://clipvista.example/t/Hx7nTrBBqLp

http://www.tidyharborhomes.example/ Please watch video to learn what we like and don’t like:
http://clipvista.example/t/vRk3QwLs

http://lorenvask.example/ Please watch video to learn what we like and don’t like:
http://clipvista.example/t/JumwdaYe

http://bluemesarugcare.example/ Please watch video to learn what we like and don’t like:
http://clipvista.example/t/TZPR8VbnX

NOTE: We do not want to copy anything outright. We want to learn, model and take their ideas and make them better. We also want to be flexible and take what we like along with your creativity to make an amazing design.

Here is what we are looking for in more specific terms:

Colors: We need to keep the teal/turquoise look of the site. But we need some contrasting colors. Also the client likes white “its clean” so we can use white space in this.

When looking at colors please know that the current site and look is NOT what we are going for. We are going for a clean and professional look but also a look that is BOLD, FUN, and Vibrant (hence the colors).

Menu: Horizontal. We like bold and easy to read menu items. Don’t make it small and cluttered.

Site Structure: Clean and easy to navigate. We have a lot of content to display so we need a clean structure that breaks up the text and content areas.

Images: Please pull images from the current site. We can always replace the images of course, but if you show them “their own stuff” in the new design you will be closer to winning because it will feel more like “them”

Look and Feel: Professional company, trusted, and makes people feel comfortable once they are there. We need to also convey clean and crisp. That is what people are looking for from them.

Content Areas: It is a safe bet that if it is on the current site we need it on the new site. So don’t drop anything as it makes it hard to “cut content”.

What we don't want: We do not want clutter, boring, or templates or themes. We don’t want too cartoony, too cute, or too fancy… Be creative!

WIREFRAME: http://clipvista.example/t/WsDhkoYz

Out of respect to professional designers who really are working hard to win if you do not follow this brief, you submit worn out themes, templates, or boring designs you will be eliminated. We are offering great prize money for this so we expect great visual designs.

We look forward to seeing your great work! Please ask any question if you have them. We will be very responsive throughout this whole contest!

Hi all, I appreciate each of you for taking the time to submit designs. I have spend a considerable amount of time today creating feedback for each of you in written and video format. We are serious about this project and are looking forward to seeing new designs. Thank you! Dale

Hi all, First I want to thank all the designers. We have many good designs and at this point are working with our client to give feedback to all of you. If we gave you feedback them please complete our requests to be considered. If you submitted a design and have not received feedback it means your design is really good, and we are sharing with our clients to get feedback so we don't waste your time on unnecessary changes. Thanks for your patience and we will get back to you soon. Dale

Reason: Hi guys, Client was on vacation and is taking a bit more time to get us feedback. Thanks, Dale

Reason: Extending to allow designers to accommodate changes for us. Dale

Target Market(s)

Most of our clients are higher end affluent. On the residential side we mostly have females calling to book appointments for our service.

We also have large businesses like apartment complexes, office buildings etc calling for our services as well.

Industry/Entity Type

Business

Font styles to use
Sans Serif

Requirements
Must have
• Space for video
Horizontal Menu
Bold
Crisp and Clean
Nice to have
• Coupons, testimonials, services,
Should not have
• cluttered
vertical menu
template look

```html
<!DOCTYPE html>
<html lang="en">
<head>
<meta charset="utf-8">
<title>Brightloom Clean – Carpet &amp; Upholstery Cleaning</title>
<link href="https://fonts.googleapis.com/css2?family=Open+Sans:wght@400;600;700;800&display=swap" rel="stylesheet">
<style>
:root{
  --green:#0b6a3b;
  --green-dark:#085530;
  --teal:#1294b5;
  --red:#e2382f;
  --ink:#444;
  --ink-soft:#777;
  --line:#ddd;
  --navy:#3a4158;
  --navy-dark:#333a4f;
  --white:#fff;
}
*{box-sizing:border-box;margin:0;padding:0}
html,body{width:1200px;height:2659px;overflow:hidden}
body{font-family:"Open Sans",Arial,sans-serif;color:var(--ink);background:var(--white);position:relative}
section,header,footer{position:absolute;left:0;width:1200px}

/* header */
.site-header{top:0;height:103px;background:var(--white)}
.brand{position:absolute;left:188px;top:18px;width:380px;height:64px}
.brand-mark{position:absolute;left:0;top:2px;width:28px;height:28px;background:var(--green)}
.brand-name{position:absolute;left:38px;top:2px;font-weight:800;font-size:24px;color:var(--teal);letter-spacing:.3px;line-height:28px;white-space:nowrap}
.brand-tag{position:absolute;left:38px;top:34px;font-size:10px;font-weight:700;color:var(--red);line-height:13px;white-space:nowrap}
.call-box{position:absolute;left:715px;top:14px;height:33px;width:170px;border:1px solid #ccc;font-size:12px;color:var(--ink-soft);display:flex;align-items:center;justify-content:center;gap:6px;white-space:nowrap}
.call-box strong{color:var(--red);font-weight:600;font-size:15px}
.social{position:absolute;left:898px;top:14px;height:33px;width:114px;border:1px solid #ccc;display:flex;align-items:center;justify-content:center;gap:8px}
.social span{width:14px;height:14px;background:#555}
.social span:first-child{background:var(--red)}
.main-nav{position:absolute;right:188px;top:64px;display:flex;gap:26px;font-size:12.5px;color:#666;white-space:nowrap}
.main-nav a{color:inherit;text-decoration:none;padding-bottom:14px}
.main-nav a.active{color:var(--red);border-bottom:3px solid var(--red)}

/* hero */
.hero{top:103px;height:423px;background:linear-gradient(100deg,#8d8f90 0%,#c8c7c3 40%,#e7e3de 70%,#f1eee9 100%)}
.hero-photo{position:absolute;inset:0}
.hero-copy{position:absolute;left:188px;top:118px;color:var(--white)}
.hero-copy .kicker{font-size:32px;font-weight:700;line-height:1}
.hero-copy h1{font-size:64px;font-weight:800;line-height:1.05;letter-spacing:1px}
.hero-copy p{font-size:11px;font-weight:600;line-height:1.5;margin-top:8px;width:230px}

/* offer band */
.offer{top:526px;height:77px;background:var(--green)}
.offer-title{position:absolute;left:188px;top:8px;color:var(--white);line-height:1.15;white-space:nowrap}
.offer-title b{display:block;font-size:21px;font-weight:800}
.offer-title span{font-size:13px;font-weight:700;display:block}
.offer-form{position:absolute;left:410px;top:18px;display:flex;gap:14px}
.field{width:162px;height:38px;border:1px solid #4f9b74;color:#cfe6d9;font-size:12px;padding:0 14px;display:flex;align-items:center;white-space:nowrap}
.submit{width:82px;height:40px;border:2px solid var(--white);color:var(--white);font-size:12px;font-weight:700;display:flex;align-items:center;justify-content:center}

/* welcome */
.welcome{top:603px;height:258px;text-align:center}
.welcome h2{position:absolute;left:0;width:1200px;top:24px;font-size:32px;font-weight:800;color:var(--ink);white-space:nowrap}
.welcome p{position:absolute;left:188px;width:824px;top:78px;font-size:10.5px;line-height:1.65;color:var(--ink-soft)}
.btn-outline{display:inline-flex;align-items:center;justify-content:center;font-size:12px;font-weight:700;border:2px solid var(--teal);color:var(--teal);height:36px;padding:0 14px;white-space:nowrap}
.welcome .btn-outline{position:absolute;left:50%;transform:translateX(-50%);top:189px}

/* services */
.services{top:861px;height:454px;background:radial-gradient(ellipse at 30% 40%,#4a4a4a,#2d2d2d 70%);color:var(--white)}
.services h2{position:absolute;top:44px;width:1200px;text-align:center;font-size:28px;font-weight:800}
.service{position:absolute;top:118px;width:170px;text-align:center}
.service .icon{width:72px;height:72px;border-radius:50%;background:rgba(255,255,255,.15);margin:0 auto;display:flex;align-items:center;justify-content:center}
.service h3{font-size:12px;font-weight:700;margin-top:38px;line-height:1.5}
.service p{font-size:10.5px;line-height:1.55;color:#ddd;margin-top:10px}
.service .btn{display:inline-flex;margin-top:22px;height:36px;padding:0 14px;align-items:center;border:1px solid #bbb;font-size:12px;font-weight:700;white-space:nowrap}
.arrow{position:absolute}

/* associations */
.associations{top:1315px;height:130px;text-align:center}
.associations h2{position:absolute;top:33px;width:1200px;font-size:15px;font-weight:700;color:#555}
.partner-row{position:absolute;left:225px;top:78px;display:flex;gap:38px}
.partner-row span{height:16px;background:#ccc;border-radius:2px}

/* why choose */
.choose{top:1445px;height:326px}
.choose-photo{position:absolute;left:0;top:0;width:500px;height:326px;background:linear-gradient(135deg,#cdc2b1,#8f8676 55%,#b8ac98)}
.choose-panel{position:absolute;left:500px;top:0;width:700px;height:326px;background:var(--teal);color:var(--white);padding:28px 0 0 46px}
.choose-panel h2{font-size:30px;font-weight:800;line-height:1;white-space:nowrap}
.choose-panel .lead{font-size:12.5px;font-weight:700;line-height:1.5;margin-top:14px;width:460px}
.ticks{list-style:none;margin-top:14px}
.ticks li{font-size:10.5px;display:flex;align-items:center;gap:10px;height:30px;white-space:nowrap}
.choose-panel .btn{display:inline-flex;margin-top:14px;height:38px;padding:0 10px;align-items:center;border:2px solid var(--white);font-size:12px;font-weight:700;white-space:nowrap}

/* testimonials */
.testimonials{top:1771px;height:413px}
.testimonials h2{position:absolute;top:36px;width:1200px;text-align:center;font-size:30px;font-weight:800;color:var(--ink);white-space:nowrap}
.quote-card{position:absolute;left:266px;top:113px;width:306px;height:208px;background:var(--green);color:var(--white);padding:30px 22px;font-size:13.5px;line-height:1.65;text-align:justify}
.video-card{position:absolute;left:626px;top:113px;width:306px;height:208px;background:linear-gradient(160deg,#8a7d6b,#c2b19a 50%,#776b5d)}
.play{position:absolute;left:123px;top:74px;width:60px;height:60px;border-radius:50%;background:var(--white);display:flex;align-items:center;justify-content:center}
.avatar{position:absolute;left:302px;top:285px;width:90px;height:90px;border-radius:50%;border:4px solid var(--white);background:linear-gradient(#c98f6e,#8a5a44);box-shadow:0 0 0 1px #ddd}
.person{position:absolute;font-size:12px;font-weight:700;color:#333;white-space:nowrap}
.person small{display:block;font-size:10px;font-weight:400;color:var(--green);margin-top:4px}

/* footer */
.site-footer{top:2184px;height:407px;background:var(--navy);color:var(--white)}
.site-footer h3{position:absolute;top:38px;font-size:18px;font-weight:700;white-space:nowrap}
.links{position:absolute;top:82px;list-style:none;width:205px}
.links li{height:37px;border-bottom:1px solid #4c5470;font-size:13px;color:#cfd3dd;display:flex;align-items:center;padding-left:2px}
.links li:last-child{border-bottom:none}
.awards{position:absolute;left:188px;top:271px;width:438px;height:99px;background:linear-gradient(90deg,#5b5f6a 0%,#7b7d82 55%,#55596a 100%)}
.awards b{position:absolute;left:12px;top:14px;font-size:16px;font-weight:800;line-height:1.2}
.awards .btn{position:absolute;left:12px;top:62px;width:90px;height:26px;border:2px solid var(--white);font-size:11px;font-weight:700;display:flex;align-items:center;justify-content:center;white-space:nowrap}
.post{position:absolute;left:665px;width:347px;height:100px;border-bottom:1px solid #4c5470}
.post.last{border-bottom:none}
.date{position:absolute;left:3px;top:2px;width:40px;height:40px;background:#575e74;text-align:center;font-size:8px;line-height:1.2;padding-top:3px}
.date b{display:block;font-size:20px;font-weight:700}
.post p{position:absolute;left:56px;top:0;width:290px;font-size:13.5px;line-height:1.55;color:#cfd3dd}
.post a{position:absolute;left:56px;top:56px;font-size:13.5px;color:var(--white);text-decoration:none}
.legal{top:2591px;height:68px;background:var(--navy-dark);color:#c7cbd6;font-size:10px}
.legal-links{position:absolute;left:188px;top:28px;display:flex;gap:10px;white-space:nowrap}
.legal-copy{position:absolute;right:188px;top:28px;white-space:nowrap}
</style>
</head>
<body>

<header class="site-header">
  <div class="brand">
    <span class="brand-mark"></span>
    <span class="brand-name">BRIGHTLOOM CLEAN</span>
    <span class="brand-tag">CARPET &amp; UPHOLSTERY CLEANING<br>24 Hour Emergency Service</span>
  </div>
  <div class="call-box">Call Us : <strong>(123) 456 -7890</strong></div>
  <div class="social" aria-label="Social links"><span></span><span></span><span></span><span></span></div>
  <nav class="main-nav">
    <a class="active">HOME</a><a>SERVICE</a><a>ABOUT US</a><a>EQUIPEMENT RENTALS</a><a>CONTACT US</a>
  </nav>
</header>

<section class="hero">
  <div class="hero-photo" role="img" aria-label="Photo of a girl lying on a soft white carpet holding a remote control"></div>
  <div class="hero-copy">
    <div class="kicker">KEEP IT</div>
    <h1>CLEAN</h1>
    <p>Brightloom clean, the best, fastest, and easiest way to clean dirty carpets!</p>
  </div>
</section>

<section class="offer">
  <div class="offer-title"><b>INTERNET SPECIAL!</b><span>THREE ROOMS CLEANED ONLY<br>$95!! LIMITED TIME OFFER!</span></div>
  <div class="offer-form">
    <div class="field">Name</div><div class="field">Email Address</div><div class="field">Phone No.</div><div class="submit">SUBMIT</div>
  </div>
</section>

<section class="welcome">
  <h2>WELCOME TO BRIGHTLOOM CLEAN</h2>
  <p>Brightloom Clean is a professional carpet cleaning company serving Albuquerque and surrounding areas. We provide the Albuquerque Metro Area with a complete and total range of residential and commercial carpet cleaning needs and services. Our carpet cleaners utilize environmentally safe cleaning methods so that you will feel safe knowing we won't be exposing your children or pets to toxic fumes or chemicals. We also provide twenty-four-hour emergency flood service, tile and grout cleaning, pet stain removal, air duct cleaning, upholstery cleaning, and much, much more! We here at Brightloom Clean, offer our 20 years of experience in carpet cleaning and we are confident in our ability to handle any situation or cleaning emergency that you may experience.</p>
  <span class="btn-outline">READ MORE</span>
</section>

<section class="services">
  <h2>OUR SERVICES</h2>
  <svg class="arrow" style="left:192px;top:110px" width="30" height="60" viewBox="0 0 30 60"><polyline points="26,4 4,30 26,56" fill="none" stroke="#1aa6d0" stroke-width="4"/></svg>
  <svg class="arrow" style="left:978px;top:110px" width="30" height="60" viewBox="0 0 30 60"><polyline points="4,4 26,30 4,56" fill="none" stroke="#1aa6d0" stroke-width="4"/></svg>
  <div class="service" style="left:269px">
    <div class="icon"><svg width="34" height="34" viewBox="0 0 34 34" fill="none" stroke="#fff" stroke-width="2.5"><path d="M12 4h6v14"/><path d="M6 18h20v6a4 4 0 0 1-4 4H10a4 4 0 0 1-4-4z"/></svg></div>
    <h3>CARPET AND UPHOLSTERY<br>CLEANING</h3>
    <p>Lorem ipsum dolor sit amet, consectetur adipiscing elit. Donec quis sagittis nibh. Vestibulum libero orci, pellentesque a mauris eu, tincidunt finibus orci.</p>
    <span class="btn">READ MORE</span>
  </div>
  <div class="service" style="left:520px">
    <div class="icon"><svg width="34" height="34" viewBox="0 0 34 34" fill="none" stroke="#fff" stroke-width="2.5"><path d="M12 4h6v14"/><path d="M6 18h20v6a4 4 0 0 1-4 4H10a4 4 0 0 1-4-4z"/></svg></div>
    <h3>TILE AND GROUT<br>CLEANING</h3>
    <p>Lorem ipsum dolor sit amet, consectetur adipiscing elit. Donec quis sagittis nibh. Vestibulum libero orci, pellentesque a mauris eu, tincidunt finibus orci.</p>
    <span class="btn">READ MORE</span>
  </div>
  <div class="service" style="left:771px">
    <div class="icon"><svg width="34" height="34" viewBox="0 0 34 34" fill="none" stroke="#fff" stroke-width="2.5"><path d="M12 4h6v14"/><path d="M6 18h20v6a4 4 0 0 1-4 4H10a4 4 0 0 1-4-4z"/></svg></div>
    <h3>STRIP AND WAX<br>FLOORS</h3>
    <p>Lorem ipsum dolor sit amet, consectetur adipiscing elit. Donec quis sagittis nibh. Vestibulum libero orci, pellentesque a mauris eu, tincidunt finibus orci.</p>
    <span class="btn">READ MORE</span>
  </div>
</section>

<section class="associations">
  <h2>ASSOCIATIONS</h2>
  <div class="partner-row" aria-label="Partner badges">
    <span style="width:98px"></span><span style="width:70px"></span><span style="width:118px"></span><span style="width:80px"></span><span style="width:66px"></span><span style="width:118px"></span>
  </div>
</section>

<section class="choose">
  <div class="choose-photo" role="img" aria-label="Photo of a vacuum cleaner head on a shaggy beige carpet"></div>
  <div class="choose-panel">
    <h2>WHY PEOPLE CHOOSE US</h2>
    <p class="lead">Lorem ipsum dolor sit amet, consectetur adipiscing elit. Donec quis sagittis nibh. Vestibulum libero orci, pellentesque a mauris eu.</p>
    <ul class="ticks">
      <li><svg width="18" height="16" viewBox="0 0 18 16"><polyline points="2,8 7,13 16,2" fill="none" stroke="#fff" stroke-width="3"/></svg>Lorem ipsum dolor sit amet, consectetur adipiscing elit. Donec quis sagittis nibh.</li>
      <li><svg width="18" height="16" viewBox="0 0 18 16"><polyline points="2,8 7,13 16,2" fill="none" stroke="#fff" stroke-width="3"/></svg>Fusce nulla orci, fringilla et ipsum vulputate, pretium tristiqu</li>
      <li><svg width="18" height="16" viewBox="0 0 18 16"><polyline points="2,8 7,13 16,2" fill="none" stroke="#fff" stroke-width="3"/></svg>Vivamus feugiat, quam nec luctus egestas, tellus felis varius era</li>
      <li><svg width="18" height="16" viewBox="0 0 18 16"><polyline points="2,8 7,13 16,2" fill="none" stroke="#fff" stroke-width="3"/></svg>Pretium turpis. Integer quis tristique urna. Curabitur sit amet turpis libero</li>
    </ul>
    <span class="btn">MAKE AN ENQUIRY</span>
  </div>
</section>

<section class="testimonials">
  <h2>WHY PEOPLE LOVE OUR SERVICES</h2>
  <svg class="arrow" style="left:186px;top:185px" width="34" height="64" viewBox="0 0 34 64"><polyline points="30,4 4,32 30,60" fill="none" stroke="#0b6a3b" stroke-width="3"/></svg>
  <svg class="arrow" style="left:974px;top:185px" width="34" height="64" viewBox="0 0 34 64"><polyline points="4,4 30,32 4,60" fill="none" stroke="#0b6a3b" stroke-width="3"/></svg>
  <div class="quote-card">“Cras facilisis pulvinar tincidunt. Maecenas bibendum varius suscipit. Quisque sit amet quam a est ornare interdum. Duis lacus mauris, cons equat at massa non,</div>
  <div class="avatar" role="img" aria-label="Customer portrait"></div>
  <div class="person" style="left:421px;top:334px">JOHN SMITH<small>New York, A Lorem Ipsum Co.</small></div>
  <div class="video-card" role="img" aria-label="Video testimonial still of a customer">
    <div class="play"><svg width="22" height="24" viewBox="0 0 22 24"><polygon points="2,0 22,12 2,24" fill="#0b6a3b"/></svg></div>
  </div>
  <div class="person" style="left:634px;top:334px">MISS RITA<small>London Heathrow, A Lorem Ipsum Co.</small></div>
</section>

<footer class="site-footer">
  <h3 style="left:188px">USEFUL LINKS</h3>
  <ul class="links" style="left:188px"><li>Home</li><li>About Us</li><li>Blog</li><li>Testimonials</li><li>Free Videos</li></ul>
  <h3 style="left:461px">LIST OF CITIES</h3>
  <ul class="links" style="left:461px;width:160px"><li>A Lorem Ipsum</li><li>A Lorem Ipsum</li><li>A Lorem Ipsum</li><li>A Lorem Ipsum</li><li>A Lorem Ipsum</li></ul>
  <div class="awards" role="img" aria-label="Photo of a silver trophy being handed over">
    <b>AWARDS &amp;<br>RECOGNITIONS</b><span class="btn">VIEW MORE</span>
  </div>
  <h3 style="left:665px">LATEST BLOG POST</h3>
  <div class="post" style="top:98px"><div class="date">Dec<b>03</b></div><p>Maecenas purus neque, tincidunt sed urna a, maximus semper nisi ut vel libero.</p><a>read more</a></div>
  <div class="post" style="top:206px"><div class="date">Dec<b>03</b></div><p>Maecenas purus neque, tincidunt sed urna a, maximus semper nisi ut vel libero.</p><a>read more</a></div>
  <div class="post last" style="top:312px"><div class="date">Dec<b>03</b></div><p>Maecenas purus neque, tincidunt sed urna a, maximus semper nisi ut vel libero.</p><a>read more</a></div>
</footer>

<section class="legal">
  <div class="legal-links"><span>TERMS</span><span>|</span><span>PRIVACY POLICY</span><span>|</span><span>TERMS AND CONDITIONS</span><span>|</span><span>SITEMAP</span></div>
  <div class="legal-copy">COPYRIGHT © 2015 BRIGHTLOOMCARPETS.EXAMPLE, ALL RIGHTS RESERVED</div>
</section>

</body>
</html>
```